Harrowgate Supply Group Business Card Design

The Business Card will be one side only with Harrowgate Supplies Group Logo
Card should have:
Name
Title
Office phone Number
Cell Number
email address
Website
Street Address
Our Slogan is Rugged and Reliable
Looking for something that stands out from other business cards

Target Market(s)

Heavy equipment Lease Company

```html
<!DOCTYPE html>
<html lang="en">
<head>
<meta charset="utf-8">
<title>Harrowgate Supplies Group – Business Card</title>
<link rel="stylesheet" href="https://fonts.googleapis.com/css2?family=Montserrat:wght@500;600;700&display=swap">
<style>
  :root {
    --backdrop: #8a8c8b;
    --card: #ffffff;
    --navy: #2b2a74;
    --red: #d31f30;
    --rule: #e4532f;
  }
  * { margin: 0; padding: 0; box-sizing: border-box; }
  html, body {
    width: 968px; height: 1200px; overflow: hidden;
    background: var(--backdrop);
    font-family: "Montserrat", sans-serif;
  }
  .card {
    position: absolute; left: 174px; top: 42px;
    width: 620px; height: 1115px;
    background: var(--card);
  }
  .brand-mark {
    position: absolute; left: 255px; top: 130px;
    width: 110px; height: 110px; border-radius: 50%;
    background: var(--navy);
  }
  .brand-name {
    position: absolute; left: 0; right: 0; top: 290px;
    color: var(--red); font-weight: 700; font-size: 36px; line-height: 44px;
    text-align: center;
  }
  .slogan {
    position: absolute; left: 0; right: 0; top: 356px;
    color: var(--navy); font-weight: 600; font-size: 22px; line-height: 28px;
    text-align: center;
  }
  .name-band {
    position: absolute; left: 0; right: 0; top: 490px; height: 65px;
    background: var(--red); color: #fff;
    font-weight: 600; font-size: 44px; line-height: 65px; text-align: center;
  }
  .title {
    position: absolute; left: 0; right: 0; top: 571px;
    color: var(--navy); font-weight: 700; font-size: 28px; line-height: 36px;
    text-align: center;
  }
  .contact-icon {
    position: absolute; left: 290px; width: 40px; height: 40px;
  }
  .contact-text {
    position: absolute; left: 0; right: 0;
    color: var(--navy); font-weight: 600; font-size: 22px; line-height: 28px;
    text-align: center;
  }
  .divider {
    position: absolute; left: 120px; width: 380px; top: 1052px;
    height: 2px; background: var(--rule);
  }
  .website {
    position: absolute; left: 0; right: 0; top: 1071px;
    color: var(--navy); font-weight: 600; font-size: 22px; line-height: 28px;
    text-align: center;
  }
</style>
</head>
<body>
  <main class="card">
    <div class="brand-mark"></div>
    <p class="brand-name">Harrowgate Supplies Group</p>
    <p class="slogan">Rugged and Reliable</p>

    <h1 class="name-band">Dana. R</h1>
    <p class="title">Manager</p>

    <svg class="contact-icon" style="top:650px" viewBox="0 0 42 42" aria-hidden="true">
      <circle cx="21" cy="21" r="21" fill="var(--navy)"/>
      <path d="M14 12c1-1 2.5-1 3.3.2l1.8 2.8c.6 1 .4 2-.4 2.7l-1.2 1c.9 2.2 2.6 3.9 4.8 4.8l1-1.2c.7-.8 1.7-1 2.7-.4l2.8 1.8c1.2.8 1.2 2.3.2 3.3l-1.4 1.4c-1.2 1.2-3.2 1.4-5.2.5C18.5 27 15 23.5 13 19.6c-.9-2-.7-4 .5-5.2z" fill="#fff"/>
    </svg>
    <p class="contact-text" style="top:697px">024.555.018</p>

    <svg class="contact-icon" style="top:745px" viewBox="0 0 42 42" aria-hidden="true">
      <circle cx="21" cy="21" r="21" fill="var(--navy)"/>
      <rect x="15" y="10" width="12" height="22" rx="2" fill="none" stroke="#fff" stroke-width="2"/>
      <line x1="19" y1="28" x2="23" y2="28" stroke="#fff" stroke-width="2"/>
    </svg>
    <p class="contact-text" style="top:797px">123.555.790</p>

    <svg class="contact-icon" style="top:837px" viewBox="0 0 42 42" aria-hidden="true">
      <circle cx="21" cy="21" r="21" fill="var(--navy)"/>
      <rect x="11" y="14" width="20" height="14" rx="1.5" fill="none" stroke="#fff" stroke-width="2"/>
      <path d="M11.5 15l9.5 7.5 9.5-7.5" fill="none" stroke="#fff" stroke-width="2"/>
    </svg>
    <p class="contact-text" style="top:887px">harrowgatesupply@mail.com</p>

    <svg class="contact-icon" style="top:925px" viewBox="0 0 42 42" aria-hidden="true">
      <circle cx="21" cy="21" r="21" fill="var(--navy)"/>
      <path d="M21 32s-7-8-7-13a7 7 0 0 1 14 0c0 5-7 13-7 13z" fill="none" stroke="#fff" stroke-width="2"/>
      <circle cx="21" cy="19" r="2.6" fill="#fff"/>
    </svg>
    <p class="contact-text" style="top:987px">W418 N1652 Alderbrook Rd, Unit D</p>

    <div class="divider"></div>
    <p class="website">www. harrowgatesupply.com</p>
  </main>
</body>
</html>
```